Fasteners Poly-bag design with KEVRA brand

We are trading with fasteners and rigging hardware and now we need a new design for a poly-bag. The header of poly-bag will contain two parts - top part (around 60%) will be static with our logo "KEVRA" and your type of design. The bottom part (around 40%) should be with different color for each group of fasteners or rigging hardware and with different text (5 groups in total). The border between the two part can be different from straight line (for example like wave or something else). I added a file with explanation and some samples of poly-bags. The total dimensions of the header are 80 mm/40 mm. The nylon part of poly-bag will have a background - I added a file with our image, but you can offer us different image also. Please when creating design, do it for full poly-bag, including the nylon part, not only header. The colors from header can continue to the nylon part also. I added a file "DESIGN SAMPLES" just as examples, what we expect to see. Of course you can offer your own variant of design! Thank you in advance!

Target Market(s)

Fasteners and rigging hardware

Industry/Entity Type

Fastener

Font styles to use
Other font styles liked:
• SAUCER BB - Logo Font

Colors

Designer to choose colors to be used in the design.

Requirements
Must have
• Our logo "KEVRA"

```html
<!DOCTYPE html>
<html lang="en">
<head>
<meta charset="utf-8">
<title>KEVRA fastener poly-bag series</title>
<link rel="stylesheet" href="https://fonts.googleapis.com/css2?family=Arimo:wght@400;700&family=Orbitron:wght@700;900&display=swap">
<style>
  :root {
    --backdrop: #9d9d9b;
    --shadow: #444444;
    --bag-film: #c6c6c4;
    --bag-edge: #d6d6d4;
    --mesh: #1e1e1e;
    --mesh-line: #2fa8e0;
    --ink: #111111;
    --accent-red: #e3171b;
    --label: #ffffff;
    --slot: #3c3c3c;
    --group-1: #2a9fdc;
    --group-2: #2a2e85;
    --group-3: #c9a26e;
    --group-4: #dede00;
  }
  * { box-sizing: border-box; margin: 0; padding: 0; }
  html, body { width: 1200px; height: 869px; overflow: hidden; }
  body {
    background: var(--backdrop);
    font-family: "Arimo", Arial, sans-serif;
    position: relative;
  }
  .bag {
    position: absolute;
    top: 204px;
    width: 202px;
    height: 409px;
  }
  .bag::before {
    content: "";
    position: absolute;
    left: 12px; top: 10px;
    width: 202px; height: 409px;
    background: var(--shadow);
  }
  .bag-1 { left: 86px;  --header: var(--group-1); }
  .bag-2 { left: 362px; --header: var(--group-2); }
  .bag-3 { left: 634px; --header: var(--group-3); }
  .bag-4 { left: 909px; --header: var(--group-4); }

  .film {
    position: absolute; inset: 0;
    background: linear-gradient(90deg, var(--bag-edge) 0 11px, var(--bag-film) 11px 193px, var(--bag-edge) 193px);
  }
  .film-art {
    position: absolute;
    left: 11px; right: 9px; top: 100px; bottom: 0;
    background: linear-gradient(160deg, #c9cbc6 0%, #bfc3bd 55%, #c7c8c4 100%);
  }
  .header {
    position: absolute; left: 0; top: 0;
    width: 202px; height: 100px;
    display: block;
  }
  .logo {
    position: absolute;
    left: 0; width: 202px; top: 36px;
    text-align: center;
    font-weight: 700;
    font-size: 20px;
    letter-spacing: 0.5px;
    color: var(--ink);
    line-height: 1;
  }
  .group-tag {
    position: absolute;
    right: 30px; top: 84px;
    font-family: "Orbitron", sans-serif;
    font-weight: 900;
    font-size: 8px;
    letter-spacing: 2.5px;
    color: var(--ink);
  }
  .group-tag .num { color: var(--accent-red); }
  .price-label {
    position: absolute;
    left: 10px; top: 110px;
    width: 184px; height: 72px;
    background: var(--label);
    border: 1px solid #8a8a8a;
    border-radius: 8px;
    text-align: center;
    color: var(--ink);
    line-height: 1;
  }
  .company { font-weight: 700; font-size: 12.5px; margin-top: 8px; letter-spacing: 0.4px; padding-left: 16px; }
  .price { font-size: 10px; margin-top: 3px; }
  .dept { font-size: 6.5px; margin-top: 1px; }
  .desc { font-size: 6.5px; margin-top: 1px; }
  .site { font-size: 6.5px; position: absolute; left: 0; right: 0; bottom: 3px; }
</style>
</head>
<body>

<section class="bag bag-1">
  <div class="film"></div>
  <div class="film-art" role="img" aria-label="Faint line illustrations of screws, nuts, bolts and washers on the clear film"></div>
  <svg class="header" viewBox="0 0 202 100" aria-hidden="true">
    <rect width="202" height="100" fill="var(--header)"/>
    <polygon points="0,66 202,50 202,72 0,92" fill="var(--mesh)"/>
    <polyline points="0,92 202,72" stroke="var(--mesh-line)" stroke-width="1" fill="none"/>
    <circle cx="101" cy="14" r="5" fill="var(--slot)" opacity="0.55"/>
    <rect x="70" y="14" width="62" height="10" rx="5" fill="var(--slot)"/>
  </svg>
  <div class="logo">KEVRA</div>
  <div class="group-tag">GROUP <span class="num">1</span></div>
  <div class="price-label">
    <p class="company">COMPANY NAME</p>
    <p class="price">$ 9.99</p>
    <p class="dept">department</p>
    <p class="desc">Product Description</p>
    <p class="site">www.website.com</p>
  </div>
</section>

<section class="bag bag-2">
  <div class="film"></div>
  <div class="film-art" role="img" aria-label="Faint line illustrations of screws, nuts, bolts and washers on the clear film"></div>
  <svg class="header" viewBox="0 0 202 100" aria-hidden="true">
    <rect width="202" height="100" fill="var(--header)"/>
    <polygon points="0,66 202,50 202,72 0,92" fill="var(--mesh)"/>
    <polyline points="0,92 202,72" stroke="var(--mesh-line)" stroke-width="1" fill="none"/>
    <circle cx="101" cy="14" r="5" fill="var(--slot)" opacity="0.55"/>
    <rect x="70" y="14" width="62" height="10" rx="5" fill="var(--slot)"/>
  </svg>
  <div class="logo">KEVRA</div>
  <div class="group-tag">GROUP <span class="num">2</span></div>
  <div class="price-label">
    <p class="company">COMPANY NAME</p>
    <p class="price">$ 9.99</p>
    <p class="dept">department</p>
    <p class="desc">Product Description</p>
    <p class="site">www.website.com</p>
  </div>
</section>

<section class="bag bag-3">
  <div class="film"></div>
  <div class="film-art" role="img" aria-label="Faint line illustrations of screws, nuts, bolts and washers on the clear film"></div>
  <svg class="header" viewBox="0 0 202 100" aria-hidden="true">
    <rect width="202" height="100" fill="var(--header)"/>
    <polygon points="0,66 202,50 202,72 0,92" fill="var(--mesh)"/>
    <polyline points="0,92 202,72" stroke="var(--mesh-line)" stroke-width="1" fill="none"/>
    <circle cx="101" cy="14" r="5" fill="var(--slot)" opacity="0.55"/>
    <rect x="70" y="14" width="62" height="10" rx="5" fill="var(--slot)"/>
  </svg>
  <div class="logo">KEVRA</div>
  <div class="group-tag">GROUP <span class="num">3</span></div>
  <div class="price-label">
    <p class="company">COMPANY NAME</p>
    <p class="price">$ 9.99</p>
    <p class="dept">department</p>
    <p class="desc">Product Description</p>
    <p class="site">www.website.com</p>
  </div>
</section>

<section class="bag bag-4">
  <div class="film"></div>
  <div class="film-art" role="img" aria-label="Faint line illustrations of screws, nuts, bolts and washers on the clear film"></div>
  <svg class="header" viewBox="0 0 202 100" aria-hidden="true">
    <rect width="202" height="100" fill="var(--header)"/>
    <polygon points="0,66 202,50 202,72 0,92" fill="var(--mesh)"/>
    <polyline points="0,92 202,72" stroke="var(--mesh-line)" stroke-width="1" fill="none"/>
    <circle cx="101" cy="14" r="5" fill="var(--slot)" opacity="0.55"/>
    <rect x="70" y="14" width="62" height="10" rx="5" fill="var(--slot)"/>
  </svg>
  <div class="logo">KEVRA</div>
  <div class="group-tag">GROUP <span class="num">4</span></div>
  <div class="price-label">
    <p class="company">COMPANY NAME</p>
    <p class="price">$ 9.99</p>
    <p class="dept">department</p>
    <p class="desc">Product Description</p>
    <p class="site">www.website.com</p>
  </div>
</section>

</body>
</html>
```